依頼詳細
店舗のイメージを崩すことなく多くのお客様へテイクアウトを開始したことを認知していただくことが目的となります。
記載項目
【店名】 濃厚豚骨醤油 らぁ麺ひなた
【メニュー】
鶏つけそば ¥830
汁なし担担麺 ¥830
辛い鶏つけそば ¥860円
激辛!汁なし担担麺 ¥860
ねぎとチャーシューの小さな丼 ¥250
温泉卵と豚そぼろの小さな丼 ¥250

【電話番号】03-5812-7406
【住所】東京都港区東山崎5-8-41 コルネ台ビル1階
【Chirpitアカウント】@noodle_hinata
【補足情報】・FoodDashyの加盟店である旨 ・電話で事前注文可能
サイズ
A6
ページ数
片面
希望イメージ
シンプル 複雑
単色 カラフル
暗い 明るい
日常 高級
遊び心 厳粛
未来的 伝統的
女性的 男性的
希望する色
赤系、黄・オレンジ系、無彩色系
補足説明
頂いたデータをプリモアにて発注する予定なので、所定の形式での納品を希望いたします。
味めぐり、Chirpit、Pictoriaなどの写真の転用OKです。
■ 選んだ理由

分かりやすさ、こちらの要望を的確に具体化してくださる柔軟性が決め手となりました。

■ 提案者全員のお礼・コメント

皆様この度たくさんのご提案誠にありがとうございました。
今回ワクモアでの発注にとても満足していますので、次回の販促物デザインも募集させて頂くことがあると思います。その時はどうぞよろしくお願いいたします。

```html
<!DOCTYPE html>
<html lang="ja">
<head>
<meta charset="utf-8">
<title>らぁ麺ひなた テイクアウト</title>
<link rel="stylesheet" href="https://fonts.googleapis.com/css2?family=Noto+Sans+JP:wght@400;500;700;900&family=Yuji+Syuku&display=swap">
<style>
  :root {
    --orange: #f39200;
    --black: #111111;
    --lime: #9fd84a;
    --white: #ffffff;
    --ink: #222222;
    --muted: #555555;
    --social: #1d9bf0;
  }
  html, body { margin: 0; padding: 0; overflow: hidden; background: var(--white); }
  .flyer {
    position: relative; width: 863px; height: 1200px; overflow: hidden;
    background: var(--white); font-family: "Noto Sans JP", sans-serif; color: var(--ink);
  }
  .header {
    position: absolute; left: 0; top: 0; width: 863px; height: 172px;
    background: var(--orange); text-align: center;
  }
  .header__title {
    position: absolute; left: 0; right: 0; top: 6px; margin: 0;
    font-weight: 900; font-size: 104px; line-height: 1; letter-spacing: 2px; color: var(--black);
  }
  .header__sub {
    position: absolute; left: 0; right: 0; top: 118px; margin: 0;
    font-weight: 700; font-size: 36px; letter-spacing: 3px; color: var(--black);
  }
  .bag { position: absolute; top: 28px; width: 90px; height: 96px; }
  .bag--left { left: 34px; }
  .bag--right { right: 34px; }
  .delivery-bar {
    position: absolute; left: 0; top: 172px; width: 863px; height: 44px;
    background: var(--black); color: var(--lime); text-align: center;
    font-weight: 700; font-size: 26px; line-height: 44px; letter-spacing: 2px;
  }
  .dish-photo { position: absolute; left: 0; top: 216px; width: 863px; height: 490px; }
  .menu { position: absolute; left: 0; top: 706px; width: 863px; }
  .menu__heading { position: absolute; left: 52px; top: 0; white-space: nowrap; }
  .menu__shop {
    font-family: "Yuji Syuku", serif; font-size: 54px; color: var(--black); letter-spacing: 2px;
  }
  .menu__label { margin-left: 40px; font-size: 24px; font-weight: 500; letter-spacing: 2px; }
  .menu__list { position: absolute; left: 0; top: 78px; width: 863px; margin: 0; padding: 0; list-style: none; }
  .menu__item {
    position: absolute; font-weight: 700; font-size: 25px; white-space: nowrap;
  }
  .menu__item::before { content: "●"; font-size: 16px; margin-right: 16px; vertical-align: 3px; }
  .menu__price { position: absolute; font-weight: 500; font-size: 20px; top: 4px; }
  .footer-social { position: absolute; left: 52px; top: 1045px; display: flex; align-items: center; }
  .footer-social__mark { width: 44px; height: 44px; border-radius: 50%; background: var(--social); }
  .footer-social__handle { margin-left: 14px; font-size: 22px; font-weight: 500; }
  .shop-info { position: absolute; left: 455px; top: 968px; width: 400px; }
  .shop-info__name { margin: 0; font-size: 27px; font-weight: 900; letter-spacing: 1px; }
  .shop-info__address { margin: 4px 0 0; font-size: 15px; font-weight: 500; }
  .shop-info__phone { margin: 6px 0 0; display: flex; align-items: center; font-size: 44px; font-weight: 900; line-height: 1; }
  .shop-info__phone svg { width: 40px; height: 40px; margin-right: 8px; }
  .shop-info__note { margin: 8px 0 0; font-size: 14px; color: var(--muted); }
</style>
</head>
<body>
<main class="flyer">
  <header class="header">
    <svg class="bag bag--left" viewBox="0 0 90 96" aria-hidden="true">
      <path d="M28 30 V20 a17 17 0 0 1 34 0 V30" fill="none" stroke="#111" stroke-width="7"/>
      <path d="M6 34 H84 L78 94 H12 Z" fill="#111"/>
    </svg>
    <h1 class="header__title">TAKE OUT</h1>
    <p class="header__sub">テイクアウトできます</p>
    <svg class="bag bag--right" viewBox="0 0 90 96" aria-hidden="true">
      <path d="M28 30 V20 a17 17 0 0 1 34 0 V30" fill="none" stroke="#111" stroke-width="7"/>
      <path d="M6 34 H84 L78 94 H12 Z" fill="#111"/>
    </svg>
  </header>
  <div class="delivery-bar">FoodDashyもご利用いただけます</div>

  <svg class="dish-photo" viewBox="0 0 863 490" role="img" aria-label="汁なし担担麺の写真:白い器に麺、肉そぼろ、白髪ねぎ、青ねぎ">
    <defs>
      <radialGradient id="bowl" cx="0.5" cy="0.5" r="0.5">
        <stop offset="0" stop-color="#c98a3a"/>
        <stop offset="0.55" stop-color="#b86a2a"/>
        <stop offset="0.8" stop-color="#e6c79a"/>
        <stop offset="0.88" stop-color="#f5f1ea"/>
        <stop offset="1" stop-color="#e9e6e0"/>
      </radialGradient>
    </defs>
    <rect width="863" height="490" fill="#ffffff"/>
    <circle cx="580" cy="250" r="340" fill="url(#bowl)"/>
  </svg>

  <section class="menu">
    <div class="menu__heading">
      <span class="menu__shop">らぁ麺 ひなた</span><span class="menu__label">テイクアウトメニュー</span>
    </div>
    <ul class="menu__list">
      <li class="menu__item" style="left:62px;top:0">鶏つけそば</li>
      <li class="menu__price" style="left:345px;top:4px">¥830</li>
      <li class="menu__item" style="left:460px;top:0">辛い鶏つけそば</li>
      <li class="menu__price" style="left:740px;top:4px">¥860</li>
      <li class="menu__item" style="left:62px;top:52px">汁なし担担麺</li>
      <li class="menu__price" style="left:345px;top:56px">¥830</li>
      <li class="menu__item" style="left:460px;top:52px">激辛!汁なし担担麺</li>
      <li class="menu__price" style="left:740px;top:56px">¥860</li>
      <li class="menu__item" style="left:62px;top:104px">ねぎとチャーシューの小さな丼</li>
      <li class="menu__price" style="left:470px;top:108px">¥250</li>
      <li class="menu__item" style="left:62px;top:156px">温泉卵と豚そぼろの小さな丼</li>
      <li class="menu__price" style="left:470px;top:160px">¥250</li>
    </ul>
  </section>

  <div class="footer-social">
    <span class="footer-social__mark"></span>
    <span class="footer-social__handle">@noodle_hinata</span>
  </div>

  <div class="shop-info">
    <p class="shop-info__name">濃厚豚骨醤油 らぁ麺ひなた</p>
    <p class="shop-info__address">東京都港区東山崎5-8-41 コルネ台ビル1階</p>
    <p class="shop-info__phone">
      <svg viewBox="0 0 24 24" aria-hidden="true"><path fill="#111" d="M6.6 10.8a15 15 0 0 0 6.6 6.6l2.2-2.2a1 1 0 0 1 1-.25 11.4 11.4 0 0 0 3.6.57 1 1 0 0 1 1 1V20a1 1 0 0 1-1 1A17 17 0 0 1 3 4a1 1 0 0 1 1-1h3.5a1 1 0 0 1 1 1c0 1.25.2 2.45.57 3.57a1 1 0 0 1-.25 1z"/></svg>
      03-5812-7406
    </p>
    <p class="shop-info__note">あらかじめご注文いただくとお受け取りがスムーズです</p>
  </div>
</main>
</body>
</html>
```